Golden Coat All-Purpose Breading Bag Design

Our client, Halvern Food Products, is looking to re-design the packaging for their product, Pellow's Golden Coat. Goldn Coat is an all-purpose food breading mix.

Halvern Foods has a registered trademark for this product, but they have not been using it for this particular 10 pound bag. They want to get the trademark onto the bag and also give the bag an updated look. They would like to continue to use the same red and blue colors. This 10 pound bag is not available on store shelves; it is sold to food service distributors who sell to restaurants.

All of the copy on the existing bag is still relevant, so we will want to incoprporate it into the bag design. Once these bags are filled with product, the tops get folded over about 1 inch and then sewn shut with thread.

Eventually, we will need the design applied to the Bag Template file attached, but that isn't important until a design is selected.

Target Market(s)

Restaurants

Industry/Entity Type

Food Manufacturing

Colors
0054AA
0677BA
7BADD7
CADEEF
E8F1F8
EB3D1F
EC4F4E
F09395
F8D3D4
FCEDEE

Requirements
Must have
• Trademark introduced to the design

```html
<!DOCTYPE html>
<html lang="en">
<head>
<meta charset="utf-8">
<title>Pellow's Golden Coat – All Purpose Breading Bag</title>
<link rel="stylesheet" href="https://fonts.googleapis.com/css2?family=Barlow:wght@400;500;700&family=Baloo+2:wght@800&display=swap">
<style>
  :root {
    --bag-blue: #110b86;
    --bag-red: #9d1b0e;
    --bag-white: #ffffff;
    --page-bg: #ffffff;
  }
  html, body {
    margin: 0;
    padding: 0;
    width: 1137px;
    height: 1200px;
    overflow: hidden;
    background: var(--page-bg);
  }
  .canvas {
    position: relative;
    width: 1137px;
    height: 1200px;
  }
  .bag {
    position: absolute;
    left: 238px;
    top: 73px;
    width: 664px;
    height: 1058px;
  }
  .bag-art {
    position: absolute;
    inset: 0;
    width: 1137px;
    height: 1200px;
  }
  .text-body { font-family: "Barlow", Arial, sans-serif; }
  .text-display { font-family: "Baloo 2", "Arial Black", sans-serif; }
  .fill-white { fill: var(--bag-white); }
  .fill-blue { fill: var(--bag-blue); }
  .fill-red { fill: var(--bag-red); }
</style>
</head>
<body>
<main class="canvas">
  <svg class="bag" viewBox="0 0 1091 1740" preserveAspectRatio="none" aria-hidden="true">
    <rect class="fill-white" x="0" y="0" width="1091" height="1740"/>
    <path class="fill-blue band-top"
          d="M0,170 C250,130 450,170 650,210 C850,250 1000,245 1091,230 V0 H0 Z"/>
    <path class="fill-red band-middle"
          d="M0,448 C250,408 450,448 650,488 C850,528 1000,523 1091,510
             V1362 C1000,1375 850,1380 650,1340 C450,1300 250,1260 0,1300 Z"/>
    <path class="fill-blue band-bottom"
          d="M0,1508 C250,1468 450,1508 650,1548 C850,1588 1000,1583 1091,1567 V1740 H0 Z"/>
  </svg>

  <svg class="bag-art" viewBox="0 0 1137 1200">
    <!-- brand name -->
    <text class="brand-name text-body fill-blue" x="304" y="290"
          font-size="70" font-weight="700" textLength="290" lengthAdjust="spacingAndGlyphs">Pellow's</text>

    <!-- company block -->
    <text class="company-name text-body fill-white" x="342" y="432"
          font-size="54" font-weight="700" textLength="190" lengthAdjust="spacingAndGlyphs">Halvern</text>
    <text class="company-line text-body fill-white" x="344" y="462"
          font-size="25" font-weight="700" textLength="196" lengthAdjust="spacingAndGlyphs">FOOD PRODUCTS</text>
    <text class="company-address text-body fill-white" x="443" y="481" text-anchor="middle"
          font-size="16" font-weight="400">4870 ORCHARD LANE</text>
    <text class="company-address text-body fill-white" x="443" y="497" text-anchor="middle"
          font-size="16" font-weight="400">CEDAR BEND, IOWA 50614</text>

    <!-- product name -->
    <text class="product-name text-display fill-white" x="306" y="646"
          font-size="128" font-weight="800" textLength="526" lengthAdjust="spacingAndGlyphs">GoldenCoat</text>
    <text class="product-tm text-body fill-white" x="836" y="568" font-size="18" font-weight="700">™</text>

    <text class="product-descriptor text-body fill-white" x="318" y="716"
          font-size="38" font-weight="700" textLength="514" lengthAdjust="spacingAndGlyphs">THE ALL PURPOSE BREADING</text>
    <text class="product-claim text-body fill-white" x="413" y="748"
          font-size="22" font-weight="400" textLength="298" lengthAdjust="spacingAndGlyphs">SEALS JUICE IN-GREASE OUT</text>

    <text class="product-slogan text-body fill-white" x="323" y="800"
          font-size="24" font-weight="400" textLength="397" lengthAdjust="spacingAndGlyphs">Chicken fried the GOLDEN COAT way</text>
    <text class="product-slogan text-body fill-white" x="323" y="825"
          font-size="24" font-weight="400" textLength="335" lengthAdjust="spacingAndGlyphs">is fried chicken the right away.</text>

    <!-- cook time -->
    <g class="icon-clock" fill="none" stroke="var(--bag-blue)" stroke-width="3" stroke-linecap="round">
      <circle cx="418" cy="897" r="12"/>
      <path d="M415,890 V901 H423"/>
    </g>
    <text class="cook-time text-body fill-blue" x="421" y="936" text-anchor="middle"
          font-size="22" font-weight="400" textLength="213" lengthAdjust="spacingAndGlyphs">Cooks two-pound chicken</text>
    <text class="cook-time text-body fill-blue" x="423" y="959" text-anchor="middle"
          font-size="22" font-weight="400" textLength="155" lengthAdjust="spacingAndGlyphs">well done in 10 min.</text>

    <!-- weight and ingredients -->
    <text class="net-weight text-body fill-red" x="859" y="962" text-anchor="end" font-size="29">
      <tspan font-weight="700">NET WT.</tspan><tspan font-weight="400"> 10 LBS.</tspan>
    </text>
    <text class="ingredients text-body fill-red" x="859" y="985" text-anchor="end" font-size="12.5">
      <tspan font-weight="700">INGREDIENTS:</tspan><tspan font-weight="400"> FLOUR, SALT, EGGS YOLK,</tspan>
    </text>
    <text class="ingredients text-body fill-red" x="859" y="998" text-anchor="end"
          font-size="12.5" font-weight="400">NON-FAT MILK SOLIDS, BAKING POWDER,</text>
    <text class="ingredients text-body fill-red" x="859" y="1011" text-anchor="end"
          font-size="12.5" font-weight="400">CORN STARCH, SUGAR AND PEPPER.</text>
  </svg>
</main>
</body>
</html>
```